Wordpress Design Project for Employee Communications Site

We need a Wordpress design for a company that strategizes on and produces materials for employee communications. Improving employee communications at all levels of an organization can help improve overall company performance and results. The site needs to look very clean and professional; we're not afraid of white space. We like the functionality that Wordpress provides; however, we only want one "true" blog page; the other pages should give the impression of a more "static" web site - particularly the home page. I have a logo that I can provide.

I have added these comments to the discussion page:
Great question - thank you for asking it. I’ve done more research

I like the very clean and monochromatic looks to many of these. I don’t have to have monochromatic, but I do like minimal colors. Simple, clean, organized. The home page should “fit” almost entirely without scrolling. I do like fat footers that you can scroll down to. I don’t want a colored background, but any that I’ve chosen with colored backgrounds could be switched to a white background.

http://www.minaveltrosk.com/
http://pondgrav.com/
http://v1.kelbrumwick.com/
http://howthemoss.com/
http://turnqualm.com/
http://www.interiors.pelmux.co.uk/
http://wrupgradstudio.com/

These last two are more corporate sites. The first one is from a well-respected consultant in my area who does a lot of what I do. And I think Farnquist does a nice job with their site. So, I want to marry the look I like with getting the content job done.

http://www.messagingkettle.com/
http://www.farnquist.com/view/en_US/us/index.htm

Target Market(s)

Target market is mid- to large-sized companies. More than 500 employees.

Industry/Entity Type

Communications

Requirements
Must have
• Need an impactful home page. There should be a "blog" page; contact us; services; about. For starters, at least. I want fonts to be very readable - that is, either quite dark gray or black.
Nice to have
• I am loathe to include a picture of myself, but I do want some images that say, "professional" and "expert" in communications.
Should not have
• I don't want a hits counter :) (I know no one would do that!).

```html
<!DOCTYPE html>
<html lang="en">
<head>
<meta charset="utf-8">
<title>Meridel Communications Company</title>
<link href="https://fonts.googleapis.com/css2?family=Oswald:wght@400;500&family=Noto+Sans:wght@400;700&family=Arimo:wght@400&display=swap" rel="stylesheet">
<style>
  :root {
    --lime: #bcd638;
    --lime-dark: #a9c52a;
    --sky: #6cc4ea;
    --ink: #2b2b2b;
    --text: #333333;
    --muted: #8c8c8c;
    --rule: #dcdcdc;
    --white: #ffffff;
  }
  * { box-sizing: border-box; margin: 0; padding: 0; }
  html, body { width: 1200px; height: 987px; overflow: hidden; background: var(--white); }
  body { position: relative; font-family: "Noto Sans", sans-serif; color: var(--text); }

  .top-band { position: absolute; left: 0; top: 0; width: 1200px; height: 11px; background: var(--lime); }

  .brand { position: absolute; left: 0; top: 44px; width: 1200px; display: flex; justify-content: center; align-items: center; gap: 14px; }
  .brand-dot { width: 34px; height: 34px; border-radius: 50%; background: var(--lime); }
  .brand-name { font-family: "Oswald", sans-serif; font-weight: 400; font-size: 38px; color: var(--lime-dark); letter-spacing: 0.5px; }

  .main-nav { position: absolute; top: 144px; left: 0; width: 1200px; height: 26px; }
  .main-nav a { position: absolute; font-family: "Oswald", sans-serif; font-size: 18px; color: var(--ink); text-decoration: none; line-height: 24px; }
  .nav-rule { position: absolute; left: 100px; top: 170px; width: 1000px; height: 8px;
    background: radial-gradient(ellipse at center top, rgba(0,0,0,0.18), rgba(0,0,0,0) 70%); }

  .slider { position: absolute; left: 297px; top: 181px; width: 627px; height: 308px; border: 1px solid #b8b8b8; overflow: hidden; }
  .slide-photo { position: absolute; inset: 0;
    background: linear-gradient(100deg, #d6dadc 0%, #c9ccc9 25%, #a9c3e0 50%, #e3e6ea 75%, #c8d8ec 100%); }
  .slide-caption { position: absolute; left: 0; top: 98px; width: 240px; height: 87px; background: var(--lime); border-radius: 0 8px 8px 0; padding: 4px 14px 0 11px; }
  .slide-caption h2 { font-family: "Oswald", sans-serif; font-weight: 400; font-size: 21px; color: var(--white); line-height: 26px; letter-spacing: -0.3px; }
  .slide-caption p { font-size: 11.5px; line-height: 15.5px; color: var(--ink); text-align: justify; }
  .slider-shadow { position: absolute; left: 210px; top: 488px; width: 800px; height: 26px;
    background: radial-gradient(ellipse at center top, rgba(0,0,0,0.22), rgba(0,0,0,0) 65%); }
  .slider-arrow { position: absolute; top: 305px; width: 30px; height: 32px; }
  .slider-arrow.prev { left: 235px; }
  .slider-arrow.next { left: 945px; }
  .slider-dots { position: absolute; top: 497px; left: 580px; display: flex; gap: 6px; }
  .slider-dots span { width: 13px; height: 13px; border-radius: 50%; background: #a7a7a7; }
  .slider-dots span.active { background: var(--sky); }

  .feature { position: absolute; width: 227px; }
  .feature h3 { font-family: "Oswald", sans-serif; font-weight: 500; font-size: 19px; color: var(--ink); line-height: 24px; letter-spacing: -0.3px; }
  .feature p { margin-top: 8px; font-size: 12px; line-height: 15.6px; color: var(--text); text-align: justify; hyphens: auto; }
  .read-more { display: flex; align-items: center; gap: 6px; margin-top: 11px; font-size: 11.5px; font-weight: 700; color: var(--ink); text-decoration: none; }
  .read-more i { width: 14px; height: 14px; border-radius: 50%; background: var(--sky); }
  .attribution { margin-top: 6px; font-size: 11.5px; line-height: 14.5px; font-weight: 700; text-align: right; color: var(--ink); }
  .col-rule { position: absolute; width: 1px; background: linear-gradient(to bottom, rgba(0,0,0,0), var(--rule), rgba(0,0,0,0)); }

  .footer-rule { position: absolute; left: 85px; top: 926px; width: 1000px; height: 12px;
    background: radial-gradient(ellipse at center top, rgba(0,0,0,0.2), rgba(0,0,0,0) 70%); }
  .footer-nav { position: absolute; top: 938px; left: 424px; font-family: "Arimo", sans-serif; font-size: 13px; color: var(--text); display: flex; gap: 0; }
  .footer-nav a { color: var(--text); text-decoration: none; }
  .footer-nav .sep { padding: 0 18px; }
  .copyright { position: absolute; top: 968px; left: 441px; font-family: "Arimo", sans-serif; font-size: 10.5px; color: var(--ink); }
  .social { position: absolute; left: 904px; top: 938px; display: flex; gap: 4px; }
  .social span { width: 34px; height: 34px; border-radius: 50%; }
  .social .one { background: var(--sky); }
  .social .two { background: var(--lime); }
</style>
</head>
<body>
  <div class="top-band"></div>

  <header class="brand">
    <span class="brand-dot"></span>
    <span class="brand-name">Meridel Communications Company</span>
  </header>

  <nav class="main-nav">
    <a href="#" style="left:359px">Home</a>
    <a href="#" style="left:459px">About</a>
    <a href="#" style="left:566px">Services</a>
    <a href="#" style="left:693px">Blog</a>
    <a href="#" style="left:788px">Contact us</a>
  </nav>
  <div class="nav-rule"></div>

  <svg class="slider-arrow prev" viewBox="0 0 30 32" aria-hidden="true"><path d="M28 0 L10 16 L28 32 L18 32 L0 16 L18 0 Z" fill="var(--lime)"/></svg>
  <svg class="slider-arrow next" viewBox="0 0 30 32" aria-hidden="true"><path d="M2 0 L20 16 L2 32 L12 32 L30 16 L12 0 Z" fill="var(--lime)"/></svg>

  <section class="slider">
    <div class="slide-photo" role="img" aria-label="Photo of colleagues reviewing notes together at a meeting table"></div>
    <div class="slide-caption">
      <h2>Effective Communication</h2>
      <p>Effective communication in the workplace is the backbone of any business.</p>
    </div>
  </section>
  <div class="slider-shadow"></div>
  <div class="slider-dots"><span class="active"></span><span></span><span></span><span></span></div>

  <article class="feature" style="left:209px; top:541px">
    <h3>External Communication</h3>
    <p>Effective communication in the workplace is the backbone of any business. Without it, you could miss out on important opportunities, waste time and cause your employees and customers to become frustrated.</p>
    <a class="read-more" href="#"><i></i>Read More</a>
  </article>
  <div class="col-rule" style="left:461px; top:560px; height:108px"></div>
  <article class="feature" style="left:488px; top:541px">
    <h3>Business Growth</h3>
    <p>Effective communication in the workplace is the backbone of any business. Without it, you could miss out on important opportunities, waste time and cause your employees and customers to become frustrated.</p>
    <a class="read-more" href="#"><i></i>Read More</a>
  </article>
  <div class="col-rule" style="left:737px; top:560px; height:108px"></div>
  <article class="feature" style="left:764px; top:541px">
    <h3>Internal Communication</h3>
    <p>Effective communication in the workplace is the backbone of any business. Without it, you could miss out on important opportunities, waste time and cause your employees and customers to become frustrated.</p>
    <a class="read-more" href="#"><i></i>Read More</a>
  </article>

  <article class="feature" style="left:209px; top:737px">
    <h3>What Customers are Saying...</h3>
    <p>MCC is a great benchmarking tool."The MCC channels offer a very effective way to communicate with geographically distributed stores and in a retail environment."</p>
    <div class="attribution">Bettina Holloway<br>Internal Communications<br>Manager</div>
  </article>
  <div class="col-rule" style="left:461px; top:760px; height:108px"></div>
  <article class="feature" style="left:488px; top:737px">
    <h3>Internal Social Media</h3>
    <p>MCC is a great benchmarking tool."The MCC channels offer a very effective way to communicate with geographically distributed stores and in a retail environment."</p>
    <div class="attribution">Specifically for employee<br>communication</div>
  </article>
  <div class="col-rule" style="left:740px; top:760px; height:108px"></div>
  <article class="feature" style="left:765px; top:737px">
    <h3>Business Growth</h3>
    <p>MCC is a great benchmarking tool."The MCC channels offer a very effective way to communicate with geographically distributed stores and in a retail environment."</p>
    <div class="attribution">Specifically for employee<br>communication</div>
  </article>

  <footer>
    <div class="footer-rule"></div>
    <nav class="footer-nav">
      <a href="#">Home</a><span class="sep">|</span>
      <a href="#">About</a><span class="sep">|</span>
      <a href="#">Services</a><span class="sep">|</span>
      <a href="#">Blog</a><span class="sep">|</span>
      <a href="#">Contact Us</a>
    </nav>
    <p class="copyright">All rights reserved. © Meridel Communications Company 2008</p>
    <div class="social" role="img" aria-label="Social network links"><span class="one"></span><span class="two"></span></div>
  </footer>
</body>
</html>
```